Human Resources consulting firm website

I recently started a consulting firm after 30 years in Human Resources (Executive Development) work with Meridian 25 companies. I am looking for a website design that will convey both the services I provide (all in the HR / executive development arena) as well as sense of trust in me and my abilities (many years of experience, breadth of knowledge).

In the attachment section, there is a document with links to a number of websites fr firms that do similar work to me - the doc shares what I like about them and what I do not. I've also include my bio to give you a sens of who I am /what I do. The head shot will be replaced soon as I'm having new photos take, but the verbiage is what's important.

I need your help with the look and feel as well as different ideas on how to share the info. I am looking for your creativity and experience. I have not done a website for anything in the past.

Looking forward to working together on a great project and product!!

Target Market(s)

Any company looking for senior leader caoching, assessments of those leaders or help with a CEO transition. My wheelhouse is Meridian top 100 companies, but am able to work with small firms as well. Also any Board of Directors and upstarts in California.

Industry/Entity Type

Consulting

Coding

Coded - Design and coding required

Number of Pages Required

5+ page

Font styles to use
Sans Serif
Other font styles liked:
• Do not have a specific one but am very open to options

Colors

Designer to choose colors to be used in the design.

Requirements
Must have
• My project must have be professional (see the type of companies I am targeting) with an air of simplicity.
• A professional yet approachable look and feel that delivers:
• (1) I want there to be a landing page (with limited info - a more of a "teaser")
• (2) a tab for about us (with a few sentences about the company, my photo and option to link to my bio)
• (3) a tab for the services offered (one page with tiles that have a little bit about the services and the option to link to more info)
• (4) a tab to contact me (form to fill out with some personal info and the request that will get sent to my email).
• (5) diversity in the imagery
• (6) I plan for it to be mostly static. I will not be adding/changing regularly (although imagine the first couple months will want to tweak it as I get feedback). I do not plan to add blogs, etc.
Nice to have
• (1) Good graphics. I'm ok with black and white if it's classic or color photos. I don't want stalk photos anyone can get on the web. A sophisticated yet approachable look is what I'm going for.
• (2) Ability to get to know me (the principal) just a bit. That can be through the verbiage, colors, photos, etc.
• (3) Ability to contact me from the front home/landing page or contact page.
• (4) When someone looks me up on line, I want them to see a sentence or two about the company and have links that will take them straight to the page on the website they are looking for (contact, about us, etc.)
Should not have
• I do not want this to be:
• (1) overly feminine (not pink, purple, etc.),
• (2) flashy (I'm fine with a small video or moving photo but doubt I want anything beyond that) or
• (3) too close to the "out there" category (this is a professional business with corporate clients).
• (4) sterile (I'm selling myself .. that's what people buy when they hire a consultant).
• (5) basic - I do not want this to look like I hired my nephew straight out of college to build this. I'm looking for a strong, professional look.

```html
<!DOCTYPE html>
<html lang="en">
<head>
<meta charset="utf-8">
<title>Alderwood Talent Partners — Contact</title>
<link rel="stylesheet" href="https://fonts.googleapis.com/css2?family=Jost:wght@400;500;600&family=Libre+Caslon+Text&display=swap">
<style>
  :root {
    --backdrop: #0c436e;
    --navy: #0e4470;
    --navy-soft: #5b8fc2;
    --ink: #1e1e1e;
    --form-band: #e8e8e8;
    --field: #ffffff;
    --footer: #333333;
    --footer-text: #c9c9c9;
    --white: #ffffff;
    --rule: #dcdcdc;
  }
  * { box-sizing: border-box; margin: 0; padding: 0; }
  html, body { width: 788px; height: 1200px; overflow: hidden; }
  body { background: var(--backdrop); font-family: "Jost", sans-serif; color: var(--ink); }

  .page {
    position: absolute; left: 64px; top: 23px;
    width: 660px; height: 1154px;
    background: var(--white);
    box-shadow: 0 6px 24px rgba(0,0,0,.3);
    overflow: hidden;
  }
  .abs { position: absolute; }

  /* header */
  .brand { left: 25px; top: 11px; height: 30px; display: flex; align-items: center; gap: 6px; }
  .brand-mark { width: 10px; height: 10px; background: var(--navy-soft); }
  .brand-name { font-size: 7.5px; line-height: 8.5px; color: var(--navy-soft); font-weight: 400; text-transform: uppercase; letter-spacing: .02em; }
  .nav { top: 21px; font-size: 7px; font-weight: 600; letter-spacing: .04em; color: var(--ink); }
  .nav.active { color: var(--navy); border-bottom: 1px solid var(--navy); padding-bottom: 2px; }
  .social-dot { top: 22px; width: 7px; height: 7px; background: var(--ink); border-radius: 1px; }

  /* intro */
  .page-title { left: 44px; top: 98px; font-family: "Libre Caslon Text", serif; font-size: 29px; color: var(--navy); font-weight: 400; }
  .page-lead { left: 44px; top: 155px; font-size: 14.5px; color: var(--ink); }

  /* form */
  .form-band { left: 0; top: 213px; width: 660px; height: 529px; background: var(--form-band); }
  .label { font-size: 8px; font-weight: 600; letter-spacing: .12em; color: var(--navy); text-transform: uppercase; }
  .field { background: var(--field); }
  .submit {
    left: 424px; top: 661px; width: 121px; height: 26px;
    background: var(--navy); color: var(--white);
    font-size: 7.5px; font-weight: 600; letter-spacing: .1em;
    display: flex; align-items: center; justify-content: center; gap: 4px;
  }

  /* reach us */
  .divider { left: 369px; top: 782px; width: 1px; height: 86px; background: var(--rule); }
  .reach-head { font-size: 8px; font-weight: 600; letter-spacing: .13em; color: var(--navy); top: 800px; }
  .reach-line { font-size: 9.5px; color: var(--ink); letter-spacing: .03em; }

  /* cta */
  .footer { left: 0; top: 991px; width: 660px; height: 163px; background: var(--footer); }
  .cta { left: 26px; top: 907px; width: 607px; height: 101px; background: var(--navy); }
  .cta-kicker { left: 28px; top: 28px; font-size: 7px; font-weight: 600; letter-spacing: .12em; color: var(--white); }
  .cta-line { left: 28px; top: 44px; font-size: 14.5px; color: var(--white); }
  .cta-button {
    left: 440px; top: 33px; width: 134px; height: 36px;
    border: 1.5px solid var(--white); color: var(--white);
    font-size: 8.5px; font-weight: 500; letter-spacing: .14em;
    display: flex; align-items: center; justify-content: center;
  }

  /* footer */
  .foot-brand { left: 38px; top: 1051px; height: 33px; display: flex; align-items: center; gap: 6px; }
  .foot-brand .brand-mark { background: var(--white); }
  .foot-brand .brand-name { color: var(--white); font-size: 8px; line-height: 9px; }
  .foot-col { top: 1054px; font-size: 7px; line-height: 15px; color: var(--footer-text); letter-spacing: .04em; }
  .foot-col .sq { display: inline-block; width: 5px; height: 5px; background: var(--footer-text); margin-right: 4px; }
</style>
</head>
<body>
  <main class="page">
    <header>
      <div class="abs brand"><span class="brand-mark"></span><span class="brand-name">Alderwood<br>Talent<br>Partners</span></div>
      <span class="abs nav" style="left:439px">ABOUT</span>
      <span class="abs nav" style="left:486px">SERVICES</span>
      <span class="abs nav active" style="left:540px">CONTACT</span>
      <span class="abs social-dot" style="left:609px" aria-label="Linkwell"></span>
      <span class="abs social-dot" style="left:626px;width:5px" aria-label="Friendbook"></span>
    </header>

    <h1 class="abs page-title">Contact</h1>
    <p class="abs page-lead">Interested in working with us? We want to hear from you!</p>

    <section class="abs form-band" aria-label="Contact form"></section>
    <span class="abs label" style="left:115px;top:270px">First name*</span>
    <span class="abs label" style="left:341px;top:270px">Last name*</span>
    <div class="abs field" style="left:115px;top:290px;width:204px;height:28px"></div>
    <div class="abs field" style="left:341px;top:290px;width:205px;height:28px"></div>

    <span class="abs label" style="left:115px;top:347px">Email address*</span>
    <div class="abs field" style="left:115px;top:368px;width:431px;height:28px"></div>

    <span class="abs label" style="left:115px;top:424px">Phone number*</span>
    <span class="abs label" style="left:341px;top:424px">Company</span>
    <div class="abs field" style="left:115px;top:445px;width:204px;height:28px"></div>
    <div class="abs field" style="left:341px;top:445px;width:205px;height:28px"></div>

    <span class="abs label" style="left:115px;top:503px">Message</span>
    <div class="abs field" style="left:115px;top:523px;width:431px;height:121px"></div>

    <div class="abs submit">SUBMIT MESSAGE
      <svg width="8" height="6" viewBox="0 0 8 6"><path d="M0 3h7M4.5 .5L7 3 4.5 5.5" stroke="#fff" stroke-width="1" fill="none"/></svg>
    </div>

    <div class="abs divider"></div>
    <span class="abs reach-head" style="left:168px">YOU MAY ALSO REACH US AT</span>
    <span class="abs reach-line" style="left:168px;top:820px">name@domain-name.com</span>
    <span class="abs reach-line" style="left:168px;top:836px">123.456.7890</span>
    <span class="abs reach-head" style="left:433px">FOLLOW US</span>
    <span class="abs reach-line" style="left:433px;top:820px">Linkwell</span>
    <span class="abs reach-line" style="left:433px;top:836px">Friendbook</span>

    <footer class="abs footer"></footer>
    <section class="abs cta">
      <span class="abs cta-kicker">CONTACT US</span>
      <span class="abs cta-line">We would love to collaborate with you</span>
      <span class="abs cta-button">GET IN TOUCH</span>
    </section>

    <div class="abs foot-brand"><span class="brand-mark"></span><span class="brand-name">Alderwood<br>Talent<br>Partners</span></div>
    <div class="abs foot-col" style="left:325px">Home<br>About<br>Services<br>Contact</div>
    <div class="abs foot-col" style="left:399px"><span class="sq"></span>Linkwell<br><span class="sq"></span>Friendbook</div>
    <div class="abs foot-col" style="left:490px">ALDERWOOD TALENT PARTNERS<br>name@domain-name.com<br>123.456.7890</div>
  </main>
</body>
</html>
```